Business Card Design

We need a new business card for our restaurant/motel as we are new owners. Our business is in a small community in a rainforest north of Townsville, Queensland AUSTRALIA and we are on a mountain 3000 feet above sea level. Visitors come here to see the wide variety of birds (This area is especially noted for the cassowary and riflebird), travel the many bush walks and enjoy the cooler climate. We would like you to use as the main colours blue and green - the buildings are painted in those colours and reflect the green for the forest and blue for the rain/sky. Yellow could also be used. The card should be bright and cheerful.
Industry/Entity Type
Travel
Contact Information for Business Card
Ferncliff Lodge Warrabee
Licensed Café/ Restaurant & Motel
14 Tallowood Lane KORRINGA Qld 4829
Ph: 07 4912 3057 Fax: 07 49123094
reception@ferncliffwarrabee.example
www.ferncliffwarrabee.example
like us on Chatterly
Look and feel
Each slider illustrates characteristics of the customer's brand and the style your logo design should communicate.

```html
<!DOCTYPE html>
<html lang="en">
<head>
<meta charset="utf-8">
<title>Ferncliff Lodge Warrabee – Business Card</title>
<link rel="stylesheet" href="https://fonts.googleapis.com/css2?family=Marcellus+SC&family=Roboto+Condensed:wght@700&family=Arimo&display=swap">
<style>
  :root {
    --card-bg: #ffffff;
    --brand-teal: #1fb9d6;
    --ink: #111111;
    --leaf-light: #8cc63f;
    --leaf-pale: #cfe6b0;
    --bark: #6b4423;
  }
  html, body {
    margin: 0;
    padding: 0;
    overflow: hidden;
    background: var(--card-bg);
  }
  .card {
    position: relative;
    width: 1200px;
    height: 900px;
    background: var(--card-bg);
    overflow: hidden;
    color: var(--ink);
  }
  .mascot-art {
    position: absolute;
    left: 45px;
    top: 135px;
    width: 455px;
    height: 465px;
  }
  .line {
    position: absolute;
    margin: 0;
    white-space: nowrap;
    line-height: 1;
  }
  .business-name {
    left: 542px;
    top: 133px;
    font-family: "Marcellus SC", serif;
    font-size: 54px;
    letter-spacing: 1px;
    color: var(--brand-teal);
  }
  .tagline {
    left: 542px;
    font-family: "Roboto Condensed", sans-serif;
    font-weight: 700;
    font-size: 35px;
  }
  .contact {
    left: 542px;
    font-family: "Arimo", sans-serif;
    font-size: 35px;
  }
  .person-name {
    left: 50px;
    top: 638px;
    font-family: "Marcellus SC", serif;
    font-size: 36px;
    letter-spacing: 2px;
    color: var(--brand-teal);
  }
  .person-title {
    left: 50px;
    top: 684px;
    font-family: "Marcellus SC", serif;
    font-size: 37px;
    letter-spacing: 2px;
    color: var(--ink);
  }
</style>
</head>
<body>
<main class="card">
  <svg class="mascot-art" viewBox="0 0 455 465" role="img" aria-label="Illustration of a green ringtail possum hanging upside down from a leafy branch">
    <defs>
      <linearGradient id="mascot-fill" x1="0" y1="0" x2="0" y2="1">
        <stop offset="0" stop-color="var(--leaf-pale)"/>
        <stop offset="1" stop-color="var(--leaf-light)"/>
      </linearGradient>
    </defs>
    <rect x="0" y="0" width="455" height="465" rx="6" fill="url(#mascot-fill)"/>
  </svg>

  <h1 class="line business-name">Ferncliff Lodge</h1>
  <p class="line tagline" style="top:205px">Warrabee Licensed</p>
  <p class="line tagline" style="top:248px">Café/ Restaurant &amp; Motel</p>

  <p class="line contact" style="top:320px">14 Tallowood Lane</p>
  <p class="line contact" style="top:369px">KORRINGA Qld 4829</p>
  <p class="line contact" style="top:441px">Ph: 07 4912 3057</p>
  <p class="line contact" style="top:501px">Fax: 07 49123094</p>
  <p class="line contact" style="top:573px">reception@ferncliffwarrabee.example</p>
  <p class="line contact" style="top:634px">www.ferncliffwarrabee.example</p>
  <p class="line contact" style="top:694px">like us on Chatterly</p>

  <p class="line person-name">Name</p>
  <p class="line person-title">Title</p>
</main>
</body>
</html>
```